qv motor spares (www.qv-motorspares.example) needs a logo box design

we need to design 2 new box for same brand with colour and same design for our company which is specialist with auto parts to be produced in china, brake pads of same brand (Taliren) the colour is Light blue or Azure and olive colour for lines the only difference between the boxes is the type which is brake pads or brake shoes only

below the logo it should be written Busan, Korea
(not made in)

all details are in the attached file

once you finish please send it as 2d and 3d pdf file

Target Market(s)

AUTO PARTS PARTS

Font styles to use
Script

Colors
33a6d7
add136

Requirements
Must have
• formula
logo
brand name
email: info@qv-motorspares.example
Nice to have
• LOGO ON THE BOX THAT STANDS FOR THE NAME OF THE BRAND
THE BRAND NAME
THE CITY OF PRODUCTION AND COUNTRY BUT WITHOUT WRITING MADE IN
THE FORMULA
SOME SAFETY RULES
ATTRACTIVE COLOURS AND DESIGNS
SOME LABELS AND ATTRACTIVE FEATURES
TAKE AS REFERENSE MORVAL BRAKE PADS BRAND

```html
<!DOCTYPE html>
<html lang="en">
<head>
<meta charset="utf-8">
<title>Taliren Brake Pads – Box Dieline</title>
<link rel="stylesheet" href="https://fonts.googleapis.com/css2?family=Questrial&display=swap">
<style>
  :root {
    --azure: #33a6d7;
    --olive: #add136;
    --navy: #0b2a5b;
    --deep-blue: #1c5ea8;
    --cyan: #2bbbe6;
    --paper: #ffffff;
    --backdrop: #e6eef7;
    --keyline: #4a4f5a;
  }
  html, body { margin: 0; padding: 0; overflow: hidden; }
  body {
    width: 1200px; height: 1200px;
    background: var(--backdrop);
    font-family: "Questrial", "Century Gothic", sans-serif;
  }
  .dieline { display: block; width: 1200px; height: 1200px; }
  .keyline { fill: var(--paper); stroke: var(--keyline); stroke-width: 1; }
  .keyline-open { fill: none; stroke: var(--keyline); stroke-width: 1; }
  .txt { font-family: "Questrial", "Century Gothic", sans-serif; }
  .brand-name { fill: var(--olive); font-weight: 700; }
  .brand-city { fill: var(--olive); font-weight: 700; letter-spacing: 1px; }
  .white { fill: #fff; }
  .olive { fill: var(--olive); }
  .rule { stroke: var(--olive); stroke-width: 2.5; }
  .rule-thin { stroke: var(--olive); stroke-width: 1; }
  .bullet { fill: #e02020; }
</style>
</head>
<body>
<svg class="dieline" viewBox="410 -120 1095 1200" preserveAspectRatio="xMidYMid meet" xmlns="http://www.w3.org/2000/svg">
  <defs>
    <linearGradient id="panel-blue" x1="0" y1="0" x2="1" y2="1">
      <stop offset="0" stop-color="#1e63b0"/>
      <stop offset="0.6" stop-color="#1f7cc4"/>
      <stop offset="1" stop-color="#2a9ad6"/>
    </linearGradient>
    <linearGradient id="pad-photo" x1="0" y1="0" x2="1" y2="1">
      <stop offset="0" stop-color="#3d5472"/>
      <stop offset="0.5" stop-color="#55627a"/>
      <stop offset="1" stop-color="#2f3f5c"/>
    </linearGradient>
    <linearGradient id="pad-small" x1="0" y1="0" x2="1" y2="0">
      <stop offset="0" stop-color="#4a4e55"/>
      <stop offset="1" stop-color="#707479"/>
    </linearGradient>
  </defs>

  <!-- Top flaps -->
  <path class="keyline" d="M590 155 V20 L612 20 V2 H905 V20 L925 20 V155 Z"/>
  <path class="keyline" d="M462 155 V45 L475 5 H570 L580 45 V155 Z"/>
  <path class="keyline" d="M945 155 V45 L955 5 H1043 L1053 45 V155 Z"/>
  <path class="keyline" d="M1062 155 L1097 40 H1358 L1390 155 Z"/>
  <path class="keyline" d="M1408 155 V162 L1500 168 V665 L1408 672 Z"/>

  <g class="top-logo">
    <circle cx="635" cy="68" r="11" class="olive"/>
    <text x="652" y="77" class="txt brand-name" font-size="26">Taliren</text>
    <text x="640" y="98" class="txt brand-city" font-size="11">Busan Korea</text>
  </g>

  <!-- Bottom flaps -->
  <path class="keyline" d="M593 818 V910 L612 945 H695 L705 935 H820 L830 945 H913 V818 Z"/>
  <path class="keyline" d="M1062 673 L1097 788 H1358 L1385 673 Z"/>
  <path class="keyline" d="M462 673 V780 L475 820 H570 L580 780 V673 Z"/>
  <path class="keyline" d="M940 673 V780 L955 822 H1043 L1053 780 V673 Z"/>

  <!-- Left side panel -->
  <g class="panel-side-left">
    <rect x="418" y="155" width="172" height="518" fill="url(#panel-blue)"/>
    <polygon points="470,155 505,155 590,420 590,520" fill="var(--cyan)"/>
    <polygon points="505,155 520,155 590,360 590,400" fill="var(--olive)"/>
    <rect x="490" y="175" width="78" height="152" rx="8" fill="url(#pad-small)" role="img" aria-label="Brake pad photograph"/>
    <rect x="462" y="498" width="86" height="130" fill="var(--navy)"/>
    <circle cx="495" cy="590" r="9" class="olive"/>
    <text transform="translate(500 580) rotate(-90)" class="txt brand-name" font-size="18">Taliren</text>
    <text transform="translate(518 585) rotate(-90)" class="txt brand-city" font-size="7">Busan Korea</text>
    <text transform="translate(537 628) rotate(-90)" class="txt white" font-size="12">Taliren Brake Pads</text>
    <path class="keyline-open" d="M462 155 V345 L425 365 V445 L462 465 H503 V365 H462 M462 465 V673"/>
  </g>

  <!-- Back panel -->
  <g class="panel-back">
    <rect x="590" y="155" width="335" height="518" fill="var(--navy)"/>
    <circle cx="636" cy="212" r="12" class="olive"/>
    <text x="654" y="222" class="txt brand-name" font-size="28">Taliren</text>
    <text x="639" y="245" class="txt brand-city" font-size="11">Busan Korea</text>
    <text x="619" y="281" class="txt white" font-size="16">Taliren Brake Pads</text>
    <line x1="620" y1="290" x2="776" y2="287" class="rule"/>
    <text x="619" y="342" class="txt white" font-size="9" font-weight="700">Disc Brake Pads</text>
    <text x="619" y="367" class="txt white" font-size="10">100% Asbestos Free</text>
    <text x="619" y="392" class="txt white" font-size="10">Limited Warranty</text>
    <text x="619" y="404" class="txt white" font-size="10">(See Retailer for Details)</text>
    <polygon points="611,420 615,423 611,426" class="bullet"/>
    <text x="619" y="426" class="txt white" font-size="9">Reduced noise with shims where applicable</text>
    <polygon points="611,436 615,439 611,442" class="bullet"/>
    <text x="619" y="442" class="txt white" font-size="9">Extended wear life and quieter operation high tech-</text>
    <text x="619" y="453" class="txt white" font-size="9">nology manufacturing</text>
    <polygon points="611,463 615,466 611,469" class="bullet"/>
    <text x="619" y="469" class="txt white" font-size="9">Consistent braking performance throughout the life</text>
    <text x="619" y="480" class="txt white" font-size="9">of the pads</text>
    <rect x="590" y="490" width="335" height="183" fill="url(#pad-photo)" role="img" aria-label="Photograph of a pair of disc brake pads"/>
    <circle cx="826" cy="560" r="11" class="olive"/>
    <text x="842" y="570" class="txt brand-name" font-size="22">Taliren</text>
    <text x="830" y="588" class="txt brand-city" font-size="9">Busan Korea</text>
    <text x="815" y="602" class="txt white" font-size="9">Taliren Brake Pads</text>
    <text x="815" y="619" class="txt white" font-size="8">info@qv-motorspares.example</text>
    <text x="815" y="629" class="txt white" font-size="8">Busan, Korea</text>
  </g>

  <!-- Narrow side panel -->
  <g class="panel-side-right">
    <rect x="925" y="155" width="132" height="518" fill="url(#panel-blue)"/>
    <polygon points="925,400 925,470 1005,673 1057,673" fill="var(--cyan)"/>
    <polygon points="925,500 925,540 990,673 1005,673" fill="var(--olive)"/>
    <rect x="990" y="177" width="67" height="148" fill="var(--navy)"/>
    <text transform="translate(971 177) rotate(90)" class="txt white" font-size="14">Taliren Brake Pads</text>
    <circle cx="1018" cy="215" r="9" class="olive"/>
    <text transform="translate(1012 230) rotate(90)" class="txt brand-name" font-size="20">Taliren</text>
    <text transform="translate(995 235) rotate(90)" class="txt brand-city" font-size="7">Busan Korea</text>
    <rect x="952" y="492" width="75" height="153" rx="8" fill="url(#pad-small)" role="img" aria-label="Brake pad photograph"/>
  </g>

  <!-- Front panel -->
  <g class="panel-front">
    <rect x="1057" y="155" width="351" height="518" fill="url(#panel-blue)"/>
    <polygon points="1408,280 1408,410 1210,673 1110,673" fill="var(--cyan)" opacity="0.85"/>
    <polygon points="1408,420 1408,470 1290,673 1250,673" fill="var(--olive)"/>
    <rect x="1077" y="155" width="170" height="75" fill="var(--navy)"/>
    <circle cx="1125" cy="196" r="12" class="olive"/>
    <text x="1143" y="206" class="txt brand-name" font-size="26">Taliren</text>
    <text x="1130" y="226" class="txt brand-city" font-size="9">Busan Korea</text>
    <text x="1076" y="259" class="txt white" font-size="25">Taliren Brake Pads</text>
    <line x1="1077" y1="269" x2="1313" y2="266" class="rule"/>
    <text x="1081" y="321" class="txt white" font-size="25" font-weight="700">Professional</text>
    <line x1="1081" y1="326" x2="1228" y2="326" class="rule-thin"/>
    <text x="1081" y="364" class="txt white" font-size="17">Disk brake pads</text>
    <text x="1081" y="377" class="txt white" font-size="11">100% Asbestos free</text>
    <line x1="1081" y1="381" x2="1228" y2="381" class="rule-thin"/>
    <text x="1081" y="404" class="txt white" font-size="10" font-weight="700">Plaquettes de freins a' disque</text>
    <text x="1081" y="417" class="txt white" font-size="11">100% sans amiante</text>
    <line x1="1081" y1="421" x2="1228" y2="421" class="rule-thin"/>
    <text x="1081" y="464" class="txt olive" font-size="22">Semi - Metalic</text>
    <rect x="1057" y="480" width="351" height="193" fill="url(#pad-photo)" opacity="0.9" role="img" aria-label="Photograph of semi-metallic brake pads"/>
  </g>

  <!-- Bottom panel -->
  <g class="panel-bottom">
    <rect x="585" y="673" width="343" height="145" fill="url(#panel-blue)"/>
    <polygon points="680,673 760,673 928,760 928,800" fill="var(--cyan)" opacity="0.7"/>
    <text transform="translate(910 727) rotate(180)" class="txt white" font-size="11">Taliren Brake Pads</text>
    <rect x="793" y="742" width="116" height="76" fill="var(--navy)"/>
    <circle cx="880" cy="765" r="9" class="olive"/>
    <text transform="translate(868 760) rotate(180)" class="txt brand-name" font-size="20">Taliren</text>
    <text transform="translate(878 748) rotate(180)" class="txt brand-city" font-size="6">Busan Korea</text>
  </g>
</svg>
</body>
</html>
```